Sales sheet for printing and embroidery apparel items - Copper Fern Prints

I would like a one page flyer or sales sheet that I would use as a template to send different images of apparel we produce. I have attached examples of layouts I like.
- Ideally, it would have space for 3-5 items.
- I would like it one page only - not a folding flyer.
- Our companies name is Copper Fern Prints.
- This will be used for many different products and markets so I don't need wording/copy. You can use wording from the 7Q7 or K81 flyer.

Colors
0054AA
0677BA
7BADD7
CADEEF
E8F1F8
00AB8E
00BBA5
67D7C9
C6EFE9
E9F9F6
FFC000
F8CF3A
FAE287
FDF2CF
FEFAEE

Requirements
Must have
• Places for between 3 and 5 images of apparel (t-shirts, hats etc)

```html
<!DOCTYPE html>
<html lang="en">
<head>
<meta charset="utf-8">
<title>Copper Fern Prints – Sales Sheet</title>
<link rel="stylesheet" href="https://fonts.googleapis.com/css2?family=Anton&family=Oswald:wght@600;700&family=Poppins:wght@500;600&display=swap">
<style>
:root{
  --stage:#a1a1a1;
  --navy:#0d3a62;
  --sky-top:#22527a;
  --sky-bottom:#0f3c63;
  --orange:#e8693a;
  --coral:#ef5f62;
  --coral-2:#e56a48;
  --coral-edge:#d63a3a;
  --white:#ffffff;
  --paper-grey:#cfcfcf;
  --ink:#1b1b1b;
  --partner:#c9ced6;
}
*{margin:0;padding:0;box-sizing:border-box}
html,body{width:861px;height:1200px;overflow:hidden;background:var(--stage)}
.flyer{position:absolute;left:122px;top:137px;width:618px;height:926px;background:var(--white);overflow:hidden;font-family:"Poppins",sans-serif}
.hero-scene{position:absolute;left:0;top:0;width:618px;height:472px;background:linear-gradient(180deg,var(--sky-top) 0%,#1a4a72 45%,var(--sky-bottom) 100%)}
.brand-corner{position:absolute;left:0;top:0}
.brand-mark{position:absolute;left:494px;top:23px;width:81px;height:71px;background:var(--orange)}
.brand-name{position:absolute;left:465px;top:98px;width:140px;text-align:center;font-family:"Oswald",sans-serif;font-weight:700;font-size:20px;line-height:21px;color:var(--navy);text-transform:uppercase}

.headline{position:absolute;left:31px;display:block;font-family:"Anton",sans-serif;font-weight:400;line-height:1;text-transform:uppercase;white-space:nowrap;text-shadow:0 2px 4px rgba(0,0,0,.35)}
.headline.l1{top:44px;font-size:57px;letter-spacing:3px;color:var(--white)}
.headline.l2{top:108px;font-size:48px;letter-spacing:1.6px;color:var(--orange)}
.headline.l3{top:162px;font-size:52px;letter-spacing:2.8px;color:var(--orange)}

.feature{position:absolute;top:240px;width:150px;text-align:center;color:var(--white)}
.feature svg{display:block;margin:0 auto;width:56px;height:56px}
.feature h3{margin-top:17px;font-family:"Anton",sans-serif;font-weight:400;font-size:19px;line-height:22px;color:var(--orange);text-transform:uppercase;white-space:nowrap}
.feature p{margin-top:4px;font-weight:500;font-size:11.5px;line-height:14px;white-space:nowrap}

.section-title{position:absolute;left:0;width:618px;text-align:center;font-family:"Anton",sans-serif;font-weight:400;text-transform:uppercase;line-height:1;white-space:nowrap}
.section-title .accent{color:var(--orange)}
.products-title{top:386px;font-size:31px;letter-spacing:1.5px;color:var(--white)}
.product-slots{position:absolute;left:31px;top:434px;display:flex;gap:7px}
.product-slot{width:108px;height:96px;background:var(--white);border:1px solid var(--navy)}

.offer-band{position:absolute;left:31px;top:565px;width:554px;height:89px;border-radius:45px;border:2px solid var(--coral-edge);background:linear-gradient(180deg,var(--coral) 0%,var(--coral-2) 100%)}
.offer-tab{position:absolute;left:240px;top:544px;width:138px;height:43px;border-radius:22px;background:var(--navy);border:2px solid var(--white);text-align:center;font-family:"Anton",sans-serif;font-size:28px;line-height:39px;color:var(--white)}
.offer-tab .accent{color:var(--orange)}
.offer-item{position:absolute;display:flex;align-items:center;gap:9px;font-weight:600;font-size:14.5px;color:var(--white);white-space:nowrap}
.offer-item svg{width:14px;height:14px;flex:none}

.order-title{top:673px;font-size:31px;color:var(--navy)}
.step-badge{position:absolute;width:48px;height:48px;border-radius:50%;border:1px solid var(--orange);display:flex;align-items:center;justify-content:center;z-index:2}
.step-badge span{width:42px;height:42px;border-radius:50%;background:var(--navy);color:var(--white);font-weight:600;font-size:19px;line-height:42px;text-align:center}
.step{position:absolute;top:716px;color:var(--ink);z-index:2}
.step h4{font-weight:500;font-size:12.5px;line-height:16px;text-transform:uppercase;white-space:nowrap}
.step p{font-weight:500;font-size:8.2px;line-height:10.7px}
.step p span{display:block;white-space:nowrap;text-align:justify;text-align-last:justify}
.step p span.last{text-align-last:left}

.torn-edge{position:absolute;left:0;top:782px;z-index:1}
.footer{position:absolute;left:0;top:832px;width:618px;height:94px;background:var(--navy)}
.footer-tagline{position:absolute;left:42px;top:846px;font-family:"Oswald",sans-serif;font-weight:600;font-size:21px;line-height:24px;color:var(--coral)}
.contact{position:absolute;left:45px;display:flex;align-items:center;gap:7px;color:var(--white);white-space:nowrap}
.contact svg{width:14px;height:14px;flex:none}
.contact.phone{top:873px;font-family:"Oswald",sans-serif;font-weight:700;font-size:21px;line-height:24px}
.contact.email{top:898px;font-weight:500;font-size:14px;line-height:18px}
.social-dots{position:absolute;left:516px;top:839px;display:flex;gap:3px}
.social-dots span{width:20px;height:20px;border-radius:50%;background:var(--coral)}
.partner-strip{position:absolute;left:282px;top:865px;width:300px;height:47px;border-radius:12px;background:var(--white);display:flex;align-items:center;justify-content:space-around;padding:0 14px}
.partner{background:var(--partner)}
.partner.round{width:28px;height:28px;border-radius:50%}
.partner.wide{width:58px;height:22px;border-radius:3px}
.partner.oval{width:40px;height:20px;border-radius:50%}
.partner.pill{width:40px;height:26px;border-radius:13px}
</style>
</head>
<body>
<main class="flyer">
  <div class="hero-scene" role="img" aria-label="Misty blue mountain ridge landscape at dusk"></div>

  <svg class="brand-corner" width="618" height="190" viewBox="0 0 618 190" aria-hidden="true">
    <path d="M433,0 H618 V154 C595,166 575,182 545,181 C510,180 472,152 450,136 C437,125 433,112 433,95 Z" fill="#ffffff"/>
  </svg>
  <div class="brand-mark"></div>
  <div class="brand-name">Copper Fern<br>Prints</div>

  <h1>
    <span class="headline l1">Order Shirts</span>
    <span class="headline l2">For Your All Of</span>
    <span class="headline l3">Your Retreats</span>
  </h1>

  <div class="feature" style="left:17px">
    <svg viewBox="0 0 60 60" fill="none" stroke="#fff" stroke-width="1.3">
      <rect x="10" y="14" width="36" height="10" rx="2"/><rect x="12" y="24" width="36" height="8" rx="2"/>
      <rect x="14" y="32" width="36" height="8" rx="2"/><rect x="16" y="40" width="36" height="8" rx="2"/>
    </svg>
    <h3>Low Minimums</h3>
    <p>Order as few as 24<br>pieces to get started.</p>
  </div>
  <div class="feature" style="left:165px">
    <svg viewBox="0 0 60 60" fill="none" stroke="#fff" stroke-width="1.3">
      <path d="M8 8 L14 10 L28 48 L56 40"/><circle cx="30" cy="52" r="4"/>
      <rect x="28" y="14" width="18" height="18" transform="rotate(-20 37 23)"/><rect x="32" y="30" width="18" height="12" transform="rotate(-20 41 36)"/>
      <path d="M4 34 H14 M2 40 H16 M6 46 H20"/>
    </svg>
    <h3>Fast Turnaround</h3>
    <p>2-week standard<br>delivery.</p>
  </div>
  <div class="feature" style="left:306px">
    <svg viewBox="0 0 60 60" fill="none" stroke="#fff" stroke-width="1.3">
      <circle cx="30" cy="18" r="6"/><circle cx="16" cy="22" r="4.5"/><circle cx="44" cy="22" r="4.5"/>
      <rect x="22" y="28" width="16" height="22" rx="5"/><rect x="9" y="30" width="12" height="16" rx="4"/><rect x="39" y="30" width="12" height="16" rx="4"/>
    </svg>
    <h3>Real People</h3>
    <p>Work with our team<br>of experts and artists.</p>
  </div>
  <div class="feature" style="left:461px">
    <svg viewBox="0 0 60 60" fill="none" stroke="#fff" stroke-width="1.3">
      <path d="M30 6 L44 12 V26 C44 36 37 42 30 45 C23 42 16 36 16 26 V12 Z"/>
      <circle cx="30" cy="25" r="8"/><path d="M26 25 L29 28 L34 22"/>
      <path d="M8 18 H12 M48 18 H52 M10 8 L13 11 M50 8 L47 11 M6 50 C14 44 22 48 28 50 H44 C48 50 52 46 56 44"/>
    </svg>
    <h3>Guaranteed</h3>
    <p>We promise accurate,<br>quality work.</p>
  </div>

  <h2 class="section-title products-title">Our <span class="accent">Products</span></h2>
  <div class="product-slots">
    <div class="product-slot" role="img" aria-label="Apparel product photo slot"></div>
    <div class="product-slot" role="img" aria-label="Apparel product photo slot"></div>
    <div class="product-slot" role="img" aria-label="Apparel product photo slot"></div>
    <div class="product-slot" role="img" aria-label="Apparel product photo slot"></div>
    <div class="product-slot" role="img" aria-label="Apparel product photo slot"></div>
  </div>

  <div class="offer-band"></div>
  <div class="offer-tab">We <span class="accent">Offer</span></div>
  <div class="offer-item" style="left:84px;top:597px"><svg viewBox="0 0 14 14"><circle cx="7" cy="7" r="7" fill="#0d3a62"/><path d="M4 7 L6.2 9.2 L10 5" stroke="#fff" stroke-width="1.6" fill="none"/></svg>Art Design</div>
  <div class="offer-item" style="left:223px;top:597px"><svg viewBox="0 0 14 14"><circle cx="7" cy="7" r="7" fill="#0d3a62"/><path d="M4 7 L6.2 9.2 L10 5" stroke="#fff" stroke-width="1.6" fill="none"/></svg>We Pay ALL Royalties to the Movement</div>
  <div class="offer-item" style="left:84px;top:625px"><svg viewBox="0 0 14 14"><circle cx="7" cy="7" r="7" fill="#0d3a62"/><path d="M4 7 L6.2 9.2 L10 5" stroke="#fff" stroke-width="1.6" fill="none"/></svg>Free Shipping</div>
  <div class="offer-item" style="left:223px;top:625px"><svg viewBox="0 0 14 14"><circle cx="7" cy="7" r="7" fill="#0d3a62"/><path d="M4 7 L6.2 9.2 L10 5" stroke="#fff" stroke-width="1.6" fill="none"/></svg>Many Options of Shirt Styles and Colors</div>

  <h2 class="section-title order-title">How To <span class="accent">Start An Order</span></h2>

  <div class="step-badge" style="left:15px;top:715px"><span>1</span></div>
  <div class="step" style="left:73px;width:127px">
    <h4>Choose Your Ride</h4>
    <p><span>Send us a picture, or let us</span><span>know the make and model</span><span>of the vehicle you would like</span><span class="last">featured on your apparel.</span></p>
  </div>
  <div class="step-badge" style="left:217px;top:715px"><span>2</span></div>
  <div class="step" style="left:275px;width:117px">
    <h4>Pick Your Gear</h4>
    <p><span>We will help you choose</span><span>your t-shirts, sweatshirts</span><span>or other apparel items</span><span>and determine sizes and</span><span class="last">quantities.</span></p>
  </div>
  <div class="step-badge" style="left:409px;top:716px"><span>3</span></div>
  <div class="step" style="left:466px;width:135px">
    <h4>We Customize</h4>
    <p><span>We make the magic happen</span><span>and our team of expert artists</span><span>will design your shirts and get</span><span>a proof out to you. Upon order</span><span>approval your order will go</span><span class="last">into production.</span></p>
  </div>

  <svg class="torn-edge" width="618" height="56" viewBox="0 0 618 56" aria-hidden="true">
    <path d="M0,12 L40,8 L70,10 L95,6 L130,14 L170,12 L210,18 L250,12 L290,16 L330,14 L370,20 L410,16 L450,18 L490,14 L530,16 L570,10 L618,14 V56 H0 Z" fill="#cfcfcf"/>
    <path d="M0,20 L30,16 L60,24 L90,22 L120,26 L150,22 L180,28 L210,22 L240,26 L270,24 L300,28 L330,24 L360,30 L390,26 L420,30 L450,26 L480,28 L510,24 L540,28 L570,22 L600,26 L618,24 V56 H0 Z" fill="#ffffff"/>
    <path d="M0,36 L22,32 L40,38 L62,34 L80,40 L104,36 L128,42 L150,38 L176,44 L200,40 L224,46 L250,38 L276,44 L300,40 L326,46 L350,40 L376,44 L400,38 L428,42 L452,36 L476,42 L500,36 L526,40 L552,34 L578,38 L600,32 L618,34 V56 H0 Z" fill="#0d3a62"/>
  </svg>
  <div class="footer"></div>

  <p class="footer-tagline">We’d love to work with you!</p>
  <p class="contact phone"><svg viewBox="0 0 14 14"><path d="M3 1.5 L5 1 L6.5 4 L5 5.2 C5.8 7 7 8.2 8.8 9 L10 7.5 L13 9 L12.5 11 C12 12.5 10.5 13 9 12.5 C5 11 3 9 1.5 5 C1 3.5 1.5 2 3 1.5 Z" fill="#e8693a"/></svg>555-218-4470</p>
  <p class="contact email"><svg viewBox="0 0 14 14"><rect x="1" y="3" width="12" height="8.5" fill="#e8693a"/><path d="M1 3 L7 8 L13 3" stroke="#0d3a62" stroke-width="1" fill="none"/></svg>orders@copperfernprints.com</p>

  <div class="social-dots" aria-hidden="true"><span></span><span></span><span></span></div>
  <div class="partner-strip" aria-label="Partner certifications">
    <span class="partner round"></span>
    <span class="partner round"></span>
    <span class="partner wide"></span>
    <span class="partner oval"></span>
    <span class="partner pill"></span>
    <span class="partner round"></span>
  </div>
</main>
</body>
</html>
```